Web Design Project

i'm looking for a sleek modern design i can use for a web site that deals with.
Clearleaf Data Capture
Accounts Payable Solutions for faster processing based on our scanning solution.
ultimately we are a intelligent scanning software.

here is a great website, that does exactly what we do, and we like to have most of their services and products.

so something in this idea would be great.
www.dravolin.com

so i guess i want a good landing/home page which is smartly designed so users will be inclined to leave their information.

and then information pages.

also i dont need any cms for you to include, i only need you to hook the html hooks for RANK Kettle as i already have a CMS and need it to hook in to that, i am including links to that cheat sheet.
so it is easier when included as you create the Theme.

http://www.rankkettle.com/how-to-create-website-template.html
http://www.rankkettle.com/cheat-sheet.html
Updates

Hi Guys sorry for the long pause in design, but here is where we stand.

what ever design i choose, i need that designer to customize a few things for me based on design that was designed.
and i will need designer to match that them to work with RANK Kettle
here is the cheat sheet for the hooks that we need to match and make it work.
if you have any questions let me know.

otherwise i look forward to working with you. and good luck.

Target Market(s)

CFO's AP Managers, mostly ppl who are not Tech freindly

Industry/Entity Type

Software

Requirements
Must have
• i need on home page, the rotating banner should have 1 ability to place vidmora links to show videos, and also ability to add buttons on these rotating banners that will allow forms to pop up take to another page.

```html
<!DOCTYPE html>
<html lang="en">
<head>
<meta charset="utf-8">
<title>Clearleaf Data Capture</title>
<link rel="stylesheet" href="https://fonts.googleapis.com/css2?family=Oswald:wght@300;400&display=swap">
<style>
:root{
  --green:#8cc63f;
  --navy:#1f3256;
  --navy-deep:#172a4a;
  --text:#333;
  --heading:#1b2a48;
  --paper:#ebebeb;
  --envelope-top:#5a9cc4;
  --envelope-bottom:#3e7ea8;
}
*{margin:0;padding:0;box-sizing:border-box}
html,body{width:1200px;height:1029px;overflow:hidden;background:#fff}
body{position:relative;font-family:Arial,Helvetica,sans-serif;color:var(--text)}

.topbar{position:absolute;left:0;top:0;width:1200px;height:27px;background:var(--green)}
.topbar__links{position:absolute;right:114px;top:5px;font-family:"Oswald",sans-serif;font-weight:300;font-size:13px;color:#fff;display:flex}
.topbar__links span{padding:0 10px}
.topbar__links span+span{border-left:1px solid #fff}

.header{position:absolute;left:0;top:27px;width:1200px;height:133px;background:linear-gradient(#3d5f93,#27406b 60%,#1c3054)}
.logo{position:absolute;left:124px;top:18px;font-family:"Oswald",sans-serif;font-weight:400;font-size:29px;line-height:31px;color:var(--green);letter-spacing:-.5px}
.phone{position:absolute;right:126px;top:5px;font-family:"Oswald",sans-serif;font-weight:400;font-size:18px;color:#fff;letter-spacing:-.3px}

.nav{position:absolute;left:112px;top:124px;width:978px;height:36px;background:linear-gradient(#2a3f63,#1a2c4b);display:flex}
.nav a{font-family:"Oswald",sans-serif;font-weight:300;font-size:14px;color:#fff;text-decoration:none;line-height:36px;padding:0 16px 0 18px;border-right:1px solid #3e5275}
.nav a.is-active{color:var(--green)}
.nav a:last-of-type{border-right:0}
.search{position:absolute;right:15px;top:7px;width:197px;height:21px;background:#fff;border:1px solid #c9c9c9;border-radius:2px;font-size:11px;line-height:19px;padding-left:8px;font-family:"Oswald",sans-serif;font-weight:300;color:#333}
.search__btn{position:absolute;right:-1px;top:-1px;width:24px;height:21px;background:var(--green)}
.accent-line{position:absolute;left:0;top:160px;width:1200px;height:5px;background:var(--green)}

.hero{position:absolute;left:112px;top:165px;width:978px;height:478px}
.hero__photo{position:absolute;inset:0;background:linear-gradient(100deg,#55708f 0%,#8fa5bc 30%,#cfd8e2 55%,#9fb3c8 75%,#e9eef2 100%)}
.hero__caption{position:absolute;left:0;top:380px;width:978px;height:98px;background:rgba(30,48,82,.92);border-top:1px dashed #cfd6e0;border-bottom:1px dashed #cfd6e0}
.hero__title{position:absolute;left:11px;top:6px;font-family:"Oswald",sans-serif;font-weight:300;font-size:44px;line-height:54px;color:var(--green);letter-spacing:-.3px}
.hero__sub{position:absolute;left:11px;top:56px;font-family:"Oswald",sans-serif;font-weight:300;font-size:22.5px;line-height:30px;color:#fff;letter-spacing:-.2px}
.arrow{position:absolute;top:344px}
.arrow--prev{left:86px}
.arrow--next{left:1090px}

.column{position:absolute;top:657px;width:257px}
.column h2{font-size:13.5px;font-weight:bold;color:var(--heading);padding-bottom:6px;border-bottom:1px solid #555;margin-bottom:8px}
.column p{font-size:11.3px;line-height:14.6px;text-align:justify}
.column p+p{margin-top:14px}
.about{left:117px}
.news{left:441px}
.news h3{font-size:11.3px;line-height:14.4px;font-weight:bold;color:var(--heading);text-align:justify}
.news .more{display:block;margin:14px 0 13px;font-size:11.3px;color:var(--heading);text-decoration:none}

.contact{position:absolute;left:812px;top:657px;width:278px;height:305px}
.contact__envelope{position:absolute;left:0;top:155px;width:278px;height:150px;background:linear-gradient(var(--envelope-top),var(--envelope-bottom))}
.contact__paper{position:absolute;left:21px;top:0;width:236px;height:240px;background:var(--paper)}
.field{position:absolute;left:24px;width:188px;background:#fff;font-family:"Oswald",sans-serif;font-weight:300;font-size:11px;color:var(--heading);padding:4px 3px}
.submit{position:absolute;left:157px;top:180px;width:55px;height:18px;background:var(--navy);border-radius:3px;color:#fff;font-family:"Oswald",sans-serif;font-weight:300;font-size:11px;line-height:18px;text-align:center}

.footer{position:absolute;left:0;top:985px;width:1200px;height:44px;background:var(--navy);display:flex;align-items:center}
.footer__title{margin-left:120px;font-size:14px;font-weight:bold;color:var(--green);margin-right:22px}
.footer a{font-family:"Oswald",sans-serif;font-weight:300;font-size:13px;color:#fff;text-decoration:none;margin-right:31px}
.footer__copy{position:absolute;right:131px;font-family:"Oswald",sans-serif;font-weight:300;font-size:12px;color:#fff}
</style>
</head>
<body>
<div class="topbar"><div class="topbar__links"><span>Blog</span><span>Sitemap</span></div></div>

<header class="header">
  <div class="logo">CLEARLEAF<br>DATA CAPTURE</div>
  <div class="phone">Call us : 123-1234576</div>
</header>

<nav class="nav">
  <a class="is-active" href="#">Products</a>
  <a href="#">Solutions</a>
  <a href="#">Services</a>
  <a href="#">Partners</a>
  <a href="#">Case Studies</a>
  <a href="#">Our Clients</a>
  <a href="#">Contact</a>
  <div class="search">Search<span class="search__btn"><svg width="24" height="21" viewBox="0 0 24 21"><circle cx="11" cy="9.5" r="4" fill="none" stroke="#fff" stroke-width="2"/><line x1="14" y1="12.5" x2="17" y2="15.5" stroke="#fff" stroke-width="2"/></svg></span></div>
</nav>
<div class="accent-line"></div>

<section class="hero">
  <div class="hero__photo" role="img" aria-label="Photo of three smiling office colleagues working at a laptop"></div>
  <div class="hero__caption">
    <div class="hero__title">ACCOUNTS PAYABLE SOLUTIONS</div>
    <div class="hero__sub">FOR FASTER PROCESSING BASED ON OUR SCANNING SOLUTION</div>
  </div>
</section>
<svg class="arrow arrow--prev" width="26" height="22" viewBox="0 0 26 22"><polygon points="26,0 0,11 26,22" fill="#7a8a5a"/><polygon points="26,4 8,11 26,18" fill="#8cc63f"/></svg>
<svg class="arrow arrow--next" width="28" height="22" viewBox="0 0 28 22"><polygon points="0,0 28,11 0,22" fill="#7a8a5a"/><polygon points="0,4 18,11 0,18" fill="#8cc63f"/></svg>

<section class="column about">
  <h2>CLEARLEAF CAPTURE</h2>
  <p>Clearleaf Capture is a leading document and data capture provider focused on helping organisations drive cost reduction and process improvement within processes such as Accounts Payable. This is achieved through a proven process of understanding and bench-marking current performance, then transforming and automating the current processes to drive cost reduction, incorporating best practices and creating 'world-class' performance.</p>
  <p>Clearleaf Capture combines best practice process knowledge and pedigree to a market-leading software suite, enabling organisations to benefit from a complete range of solutions from paper scanning through to intelligent, template-free data extraction and the ability to receipt purchase invoices irrespective of format (EDI, XML, PDF, email).</p>
</section>

<section class="column news">
  <h2>LATEST NEWS</h2>
  <h3>Clearleaf Capture Shortlisted for National Finance Awards 2012</h3>
  <p>Clearleaf Capture has been shortlisted for the Software Product of the Year category at the prestigious National Finance Awards 2012.</p>
  <a class="more" href="#">read more»</a>
  <h3>Harrow Bakes drives Purchase-to-Pay efficiency with "touchless" invoice processing</h3>
  <p>Clearleaf Capture and strategic business partner NORD7 Business Software, the UK division of global business software group NORD7, today announced that Harrow Bakes has implemented the Billflow hybrid invoice processing solution, delivering 100% of its invoices electronically into Harrow's existing NORD7 Ledger Financials system.</p>
  <a class="more" href="#">read more»</a>
</section>

<aside class="contact">
  <div class="contact__envelope" role="img" aria-label="Illustration of an open blue envelope holding the contact form"></div>
  <div class="contact__paper">
    <div class="field" style="top:21px;height:21px">NAME</div>
    <div class="field" style="top:54px;height:21px">E-MAIL</div>
    <div class="field" style="top:88px;height:87px">MESSAGE</div>
    <div class="submit">SUBMIT</div>
  </div>
</aside>

<footer class="footer">
  <span class="footer__title">QUICK LINKS</span>
  <a href="#">Products</a><a href="#">Solutions</a><a href="#">Services</a><a href="#">Partners</a><a href="#">Case Studies</a><a href="#">Our Clients</a><a href="#">Contact</a>
  <span class="footer__copy">© Clearleaf Capture 2012</span>
</footer>
</body>
</html>
```